I need a cover for a brochure made

I need a cover for a brochure. The dimensions are 8.25 wide and 5.25 high... I also need a .25 inch bleed outside of those dimensions.

I need it to look like a vintage photo album cover. In big words, I would like it to say "Family". Above it in smaller words "To our Harlow Fairway" ... making it look like the words are gold inlay or something.

I would like it kind of in the style of some of the attached maybe. Just vintage looking.

```html
<!DOCTYPE html>
<html lang="en">
<head>
<meta charset="utf-8">
<title>Family – Brochure Cover</title>
<link rel="stylesheet" href="https://fonts.googleapis.com/css2?family=Rye&family=Sancreek&display=swap">
<style>
  :root {
    --leather-dark: #5a2a0c;
    --leather-mid: #8a4512;
    --leather-light: #a8581a;
    --gilt-dark: #6e4422;
    --gilt-mid: #9c6a3c;
    --gilt-light: #c59a62;
    --parchment-light: #f8f1dc;
    --parchment-mid: #e6d3a2;
    --parchment-edge: #9a7240;
    --ink: #4e1f1c;
  }
  html, body {
    margin: 0;
    padding: 0;
    width: 1200px;
    height: 764px;
    overflow: hidden;
    background: var(--leather-dark);
  }
  .cover {
    position: relative;
    width: 1200px;
    height: 764px;
    overflow: hidden;
    background: radial-gradient(ellipse at 50% 50%, var(--leather-light) 0%, var(--leather-mid) 55%, var(--leather-dark) 100%);
  }
  .scroll-frame {
    position: absolute;
    left: 8px;
    top: 4px;
    width: 1184px;
    height: 756px;
    border-radius: 60px;
    background: linear-gradient(135deg, var(--gilt-light) 0%, var(--gilt-mid) 35%, var(--gilt-dark) 65%, var(--gilt-mid) 100%);
  }
  .parchment {
    position: absolute;
    left: 120px;
    top: 105px;
    width: 960px;
    height: 555px;
    background: radial-gradient(ellipse at 50% 52%, var(--parchment-light) 0%, var(--parchment-mid) 60%, var(--parchment-edge) 100%);
  }
  .title {
    position: absolute;
    left: 0;
    top: 290px;
    width: 1200px;
    margin: 0;
    text-align: center;
    color: var(--ink);
    font-weight: 400;
  }
  .title-lead {
    display: block;
    font-family: "Rye", serif;
    font-size: 46px;
    line-height: 64px;
    letter-spacing: 1px;
    margin-left: 6px;
  }
  .title-main {
    display: block;
    font-family: "Sancreek", serif;
    font-size: 172px;
    line-height: 170px;
    letter-spacing: 4px;
    margin-top: 4px;
    text-shadow: 0 4px 8px rgba(90, 50, 20, 0.35);
  }
</style>
</head>
<body>
  <main class="cover">
    <div class="scroll-frame" role="img" aria-label="Carved gilt acanthus scroll frame surrounding the cover"></div>
    <div class="parchment" role="img" aria-label="Aged parchment panel"></div>
    <h1 class="title">
      <span class="title-lead">TO OUR HARLOW FAIRWAY</span>
      <span class="title-main">FAMILY</span>
    </h1>
  </main>
</body>
</html>
```